Label design for ecological olive oil from an innovative farm in Spain

EL PRADO SOLAR - Olive Oil Label
El Prado Solar is a small farm in southern Spain dedicated to regenerative, ecological and syntropic agriculture. We are launching a new extra virgin olive oil and, alongside it, a renewed brand identity that reflects our relationship with land, life and earth.
Our farm works as a living food forest: diverse, dense, colourful and abundant. This is not industrial organic farming — it is ecosystem regeneration in action. We are looking for a label that feels:
* Lush, abundant and alive
* Nature-connected and animist (the land as a living being)
* Sunny Mediterranean (southern Spain, warmth, light, joy)
* Upbeat and playful, not austere or “eco-serious”
* Slightly rebellious, non-corporate, non-industrial
This is an olive oil for people who care deeply about the planet, but who also love beauty, colour and pleasure.
We are particularly drawn to designs that express the visual richness and lushness of our syntropic food forest:
* Dense, layered plant life
* Multiple tree species growing together
* A sense of abundance
* A “window into a living world” feeling
Tree species present on the farm include:
* Olive
* Citrus
* Pomegranate
* Fig
* Almond
We welcome designs with illustrative approaches that feel hand-drawn, painterly or slightly retro. We are open to interpretation — the goal is to transmit aliveness, not literal realism.
We currently use Montserrat font and are happy to continue with it or something similar.
We are also open to retro-inspired or softer typefaces, provided they feel natural, warm and not corporate.
We want to avoid plastic labels. The design should work with:
* Uncoated/organic paper labels, or
* Direct printing or screen printing onto glass
The label should feel tactile and natural.
We have uploaded :
* Final front and back label text (Spanish + English)
* Logo
* Reference images (AI explorations, farm photos, landscape, food forest)
The olive oil will be sold in Spain and internationally, so bilingual clarity is important.
Our business logo should be used but does not need to dominate the front label.
It may work better subtly placed, possibly on the back label or integrated quietly into the design.
A successful label will feel like:
* A living landscape captured on a bottle
* Something joyful, rooted and contemporary
* A product of land, care and imagination — not marketing
We want people to feel, instinctively:
This oil comes from a place that is alive.

```html
<!DOCTYPE html>
<html lang="es">
<head>
<meta charset="utf-8">
<title>El Prado Solar – Olive Oil Labels</title>
<link rel="stylesheet" href="https://fonts.googleapis.com/css2?family=Fraunces:opsz,wght@9..144,600;9..144,800&family=Montserrat:ital,wght@0,400;0,600;0,700;1,400&display=swap">
<style>
  :root {
    --backdrop: #16110a;
    --sun-top: #fbe08a;
    --sun-mid: #f5b54a;
    --sun-low: #e8843f;
    --terracotta: #cf5b34;
    --frame-green: #3d5a1e;
    --frame-light: #8fae45;
    --ink-green: #24380f;
    --ink-accent: #7a1f14;
    --forest-olive: #6f9a2e;
    --forest-deep: #2f5a1a;
    --forest-citrus: #f28c1c;
    --forest-pomegranate: #c0322a;
    --forest-fig: #6b3a5a;
    --forest-almond: #f6e3c8;
  }
  * { box-sizing: border-box; margin: 0; padding: 0; }
  html, body { width: 1200px; height: 1040px; overflow: hidden; background: var(--backdrop); }
  body { font-family: "Montserrat", Arial, sans-serif; color: var(--ink-green); }

  .label-sheet {
    width: 1200px; height: 1040px;
    display: flex; justify-content: center; align-items: center; gap: 90px;
  }
  .label { position: relative; width: 420px; height: 880px; }
  .label-frame { position: absolute; inset: 0; width: 100%; height: 100%; }
  .label-content {
    position: absolute; inset: 56px 40px 50px;
    display: flex; flex-direction: column; align-items: center; text-align: center;
  }

  /* Food-forest windows */
  .forest-window {
    border-radius: 50% 50% 44% 44% / 56% 56% 44% 44%;
    background:
      radial-gradient(circle at 24% 40%, var(--forest-citrus) 0 7%, transparent 14%),
      radial-gradient(circle at 72% 34%, var(--forest-pomegranate) 0 6%, transparent 13%),
      radial-gradient(circle at 58% 70%, var(--forest-fig) 0 5%, transparent 12%),
      radial-gradient(circle at 38% 22%, var(--forest-almond) 0 5%, transparent 11%),
      radial-gradient(ellipse at 50% 60%, var(--forest-olive) 0%, var(--forest-deep) 62%, rgba(47,90,26,0) 74%);
  }

  /* Front label */
  .brand-name {
    font-family: "Fraunces", Georgia, serif;
    font-weight: 800; color: var(--ink-accent);
    line-height: 1.05; margin-top: 10px;
  }
  .brand-name .brand-small { display: block; font-size: 36px; }
  .brand-name .brand-large { display: block; font-size: 46px; }
  .product-title {
    font-family: "Fraunces", Georgia, serif;
    font-weight: 800; font-size: 52px; color: var(--frame-green);
    letter-spacing: 2px; margin-top: 28px;
  }
  .forest-front { width: 300px; height: 200px; margin-top: 8px; }
  .front-lines { margin-top: 40px; display: flex; flex-direction: column; align-items: center; }
  .front-lines .line-es { font-size: 16px; font-weight: 600; }
  .front-lines .line-en { font-size: 16px; margin-top: 18px; }
  .front-lines .line-intro { font-size: 16px; margin-top: 4px; }
  .front-lines .line-practice { font-size: 17px; font-weight: 700; color: var(--ink-accent); margin-top: 26px; }
  .front-lines .line-grown { font-size: 17px; line-height: 1.45; margin-top: 6px; }
  .volume { font-family: "Fraunces", Georgia, serif; font-weight: 600; font-size: 34px; color: var(--ink-green); margin-top: 18px; }

  /* Back label */
  .back-content { inset: 48px 36px 50px; }
  .forest-back { width: 250px; height: 170px; }
  .back-text { font-size: 11px; line-height: 1.4; margin-top: 50px; }
  .back-text p { margin-bottom: 11px; }
  .back-text .gap-large { margin-top: 32px; }
  .back-text strong { color: var(--ink-accent); font-weight: 700; }
  .back-text em { font-style: italic; }
  .back-text .fine { font-size: 9.5px; line-height: 1.4; }
</style>
</head>
<body>
<main class="label-sheet">

  <section class="label label-back" aria-label="Etiqueta trasera">
    <svg class="label-frame" viewBox="0 0 420 880" aria-hidden="true">
      <defs>
        <linearGradient id="backFill" x1="0" y1="0" x2="0" y2="1">
          <stop offset="0" stop-color="var(--sun-top)"/>
          <stop offset="0.55" stop-color="var(--sun-mid)"/>
          <stop offset="1" stop-color="var(--sun-low)"/>
        </linearGradient>
      </defs>
      <path d="M 40 20 Q 210 -5 380 20 A 30 30 0 0 0 410 50 L 410 830 A 30 30 0 0 0 380 860 Q 210 885 40 860 A 30 30 0 0 0 10 830 L 10 50 A 30 30 0 0 0 40 20 Z"
            fill="url(#backFill)" stroke="var(--frame-green)" stroke-width="6"/>
      <path d="M 50 34 Q 210 12 370 34 A 26 26 0 0 0 396 60 L 396 820 A 26 26 0 0 0 370 846 Q 210 868 50 846 A 26 26 0 0 0 24 820 L 24 60 A 26 26 0 0 0 50 34 Z"
            fill="none" stroke="var(--frame-light)" stroke-width="2" stroke-dasharray="2 5" stroke-linecap="round"/>
    </svg>
    <div class="label-content back-content">
      <div class="forest-window forest-back" role="img" aria-label="Ilustración de bosque comestible con olivo, cítricos, granado, higuera y almendro"></div>
      <div class="back-text">
        <p>Aceite de oliva de categoría superior obtenido directamente<br>de aceitunas y solo mediante procedimientos mecánicos.</p>
        <p>Origen: <strong>Almendral Alto, Granada, España</strong></p>
        <p>Edición limitada de la finca única<br>Elaborado y envasado por:<br><strong>Fundación El Prado Solar</strong><br><em>Proyecto agrícola dedicado a la regeneración<br>de ecosistemas y al cuidado de la tierra y las personas.</em><br>Recolectado a mano</p>
        <p class="gap-large">Prensado en frío, menos de un día<br>tras la cosecha</p>
        <p>Limited edition from a single farm<br>Produced and bottled by:<br><strong>Fundación El Prado Solar</strong><br><em>An agricultural project dedicated to ecosystem<br>regeneration and the care of land and people.</em></p>
        <p class="fine">Hand picked and cold pressed<br>within one day of harvest</p>
        <p class="fine">Variedad: <strong>Picual · Manzanilla · Acebuche (Wild Olive)</strong><br>Sin filtrar<br>Conservar en lugar fresco y protegido de la luz.</p>
        <p class="fine">Lote: Otoño 2025<br>Consumir preferentemente antes de: 05/2027</p>
      </div>
    </div>
  </section>

  <section class="label label-front" aria-label="Etiqueta frontal">
    <svg class="label-frame" viewBox="0 0 420 880" aria-hidden="true">
      <defs>
        <linearGradient id="frontFill" x1="0" y1="0" x2="0" y2="1">
          <stop offset="0" stop-color="var(--sun-top)"/>
          <stop offset="0.55" stop-color="var(--sun-mid)"/>
          <stop offset="1" stop-color="var(--sun-low)"/>
        </linearGradient>
      </defs>
      <path d="M 40 20 Q 210 -5 380 20 A 30 30 0 0 0 410 50 L 410 830 A 30 30 0 0 0 380 860 Q 210 885 40 860 A 30 30 0 0 0 10 830 L 10 50 A 30 30 0 0 0 40 20 Z"
            fill="url(#frontFill)" stroke="var(--frame-green)" stroke-width="6"/>
      <path d="M 50 34 Q 210 12 370 34 A 26 26 0 0 0 396 60 L 396 820 A 26 26 0 0 0 370 846 Q 210 868 50 846 A 26 26 0 0 0 24 820 L 24 60 A 26 26 0 0 0 50 34 Z"
            fill="none" stroke="var(--frame-light)" stroke-width="2" stroke-dasharray="2 5" stroke-linecap="round"/>
    </svg>
    <div class="label-content">
      <h1 class="brand-name"><span class="brand-small">El</span><span class="brand-large">Prado Solar</span></h1>
      <h2 class="product-title">OLIVE OILS</h2>
      <div class="forest-window forest-front" role="img" aria-label="Ilustración de un bosque comestible soleado con olivos, naranjos, granados, higueras y almendros"></div>
      <div class="front-lines">
        <p class="line-es">Aceite de Oliva Virgen Extra</p>
        <p class="line-en">Extra Virgin Olive Oil</p>
        <p class="line-intro">Cultivado con practicas de la</p>
        <p class="line-practice">agricultura regenerativa y sintrópica</p>
        <p class="line-grown">Grown using regenerative and<br>syntropic farming practices</p>
      </div>
      <p class="volume">500ml</p>
    </div>
  </section>

</main>
</body>
</html>
```